GPB New Busines Card

we need a business card for or renovation company, our main color is orange and our logo is a concrete ball rolling with GPB on it.the company name is Granite Path Builders, Inc, we need somthing simple but profecional, also that we can change if its for roofing or renovations and the names

Target Market(s)

home owners

Industry/Entity Type

Concrete

Contact Information for Business Card

Colors
f68d4d
f9ba93
f37122
f78f20
faa54b
fbc994

```html
<!DOCTYPE html>
<html lang="en">
<head>
<meta charset="utf-8">
<title>Granite Path Builders – Business Card</title>
<link href="https://fonts.googleapis.com/css2?family=Orbitron:wght@600&family=Didact+Gothic&family=Mulish:wght@700&display=swap" rel="stylesheet">
<style>
  :root {
    --stage: #8a8a8a;
    --card-white: #ffffff;
    --ink: #111111;
    --band: #0d0d0d;
    --orange-deep: #f37122;
    --orange-mid: #f78f20;
    --orange-light: #faa54b;
    --orange-pale: #fbc994;
    --stone: #9a9189;
    --silver: #c9c9c9;
  }
  * { margin: 0; padding: 0; box-sizing: border-box; }
  html, body { width: 1200px; height: 900px; overflow: hidden; }
  body {
    background: linear-gradient(180deg, #a9a9a9 0%, var(--stage) 100%);
    display: flex; align-items: center; justify-content: center;
    font-family: "Didact Gothic", sans-serif; color: var(--ink);
  }
  .card {
    position: relative; width: 1000px; height: 571px;
    border-radius: 34px; overflow: hidden;
    background: var(--card-white);
    box-shadow: 0 18px 40px rgba(0,0,0,.35);
  }
  .brand-area { position: absolute; inset: 0 0 auto 0; height: 300px; }
  .brand-dot {
    position: absolute; left: 170px; top: 62px; width: 176px; height: 176px;
    border-radius: 50%; background: var(--stone);
  }
  .brand-name {
    position: absolute; left: 385px; top: 86px;
    font-family: "Orbitron", sans-serif; font-weight: 600;
    font-size: 50px; line-height: 66px; letter-spacing: 1px; color: var(--ink);
  }
  .brand-ghost {
    position: absolute; right: -70px; top: 40px; width: 210px; height: 210px;
    border-radius: 50%; background: #ececec;
  }
  .service-band {
    position: absolute; left: 0; right: 0; top: 300px; height: 42px;
    background: var(--band); border-bottom: 5px solid var(--silver);
    display: flex; justify-content: space-around; align-items: center;
    font-family: "Orbitron", sans-serif; font-weight: 600;
    font-size: 20px; letter-spacing: 7px; color: var(--orange-mid);
  }
  .contact-area {
    position: absolute; left: 0; right: 0; top: 347px; bottom: 0;
    background: linear-gradient(180deg, var(--orange-light) 0%, var(--orange-mid) 45%, var(--orange-deep) 100%);
  }
  .rep { position: absolute; left: 60px; top: 38px; width: 380px; text-align: center; }
  .rep-name { font-family: "Mulish", sans-serif; font-weight: 700; font-size: 32px; }
  .rep-title { font-family: "Mulish", sans-serif; font-weight: 700; font-size: 20px; margin-top: 2px; }
  .assurances {
    position: absolute; left: 50px; top: 140px; width: 400px; text-align: center;
    font-size: 19px; letter-spacing: 5px; line-height: 30px;
  }
  .divider { position: absolute; left: 480px; top: 22px; width: 2px; height: 182px; background: #3a2a1a; }
  .contacts { position: absolute; left: 505px; top: 18px; list-style: none; font-size: 19px; line-height: 29px; }
  .contacts li { display: flex; align-items: center; gap: 8px; }
  .contacts svg { width: 18px; height: 18px; flex: none; fill: var(--ink); }
  .contacts .indent { padding-left: 26px; }
</style>
</head>
<body>
  <div class="card">
    <div class="brand-area">
      <div class="brand-ghost"></div>
      <div class="brand-dot"></div>
      <div class="brand-name">GRANITE PATH<br>BUILDERS</div>
    </div>

    <div class="service-band">
      <span>ROOFING</span><span>PAINTING</span><span>RENOVATIONS</span>
    </div>

    <div class="contact-area">
      <div class="rep">
        <div class="rep-name">Marisol Vega</div>
        <div class="rep-title">Sales Representative</div>
      </div>
      <div class="assurances">FREE ESTIMATES<br>LICENSED &amp; INSURED</div>
      <div class="divider"></div>
      <ul class="contacts">
        <li><svg viewBox="0 0 18 18"><rect x="5" y="1" width="8" height="16" rx="1.5"/><rect x="6.5" y="3" width="5" height="9" fill="#faa54b"/></svg>555-201-4830</li>
        <li><svg viewBox="0 0 18 18"><path d="M3 2l3-1 2 4-2 2c1 2.5 3 4.5 5 5l2-2 4 2-1 3c-7 1-14-6-13-13z"/></svg>555-377-1962</li>
        <li><svg viewBox="0 0 18 18"><rect x="2" y="7" width="14" height="8" rx="1"/><rect x="5" y="2" width="8" height="6"/><rect x="5" y="11" width="8" height="2" fill="#faa54b"/></svg>555-604-2718</li>
        <li><svg viewBox="0 0 18 18"><rect x="1" y="4" width="16" height="11" rx="1"/><path d="M1.5 4.5L9 10l7.5-5.5" stroke="#faa54b" stroke-width="1.5" fill="none"/></svg>Marisol@GranitePathBuilders.com</li>
        <li><svg viewBox="0 0 18 18"><circle cx="9" cy="9" r="7.5" fill="none" stroke="#111" stroke-width="1.5"/><ellipse cx="9" cy="9" rx="3.2" ry="7.5" fill="none" stroke="#111" stroke-width="1.2"/><path d="M1.5 9h15M3 5h12M3 13h12" stroke="#111" stroke-width="1.2"/></svg>www.GranitePathBuilders.com</li>
        <li><svg viewBox="0 0 18 18"><path d="M9 1L1 8h2.5v8h4v-5h3v5h4V8H17z"/></svg>418 Quarry Stone Ln</li>
        <li class="indent">Millbrook, GA 30000</li>
      </ul>
    </div>
  </div>
</body>
</html>
```